Internet Of Things brochure

Need to create a brochure with a common theme to our website and the last 2 pages of the attached file. All the contect is in the file that I have attached.
website www.norvalenetworks.com.au

Industry/Entity Type

Internet

```html
<!DOCTYPE html>
<html lang="en">
<head>
<meta charset="utf-8">
<title>Norvale Networks Brochure</title>
<link rel="stylesheet" href="https://fonts.googleapis.com/css2?family=Exo+2:wght@400;500;600;700&display=swap">
<style>
  :root {
    --stage: #a9e3dc;
    --ink: #14161c;
    --page-light-top: #eef1f5;
    --page-light-mid: #cfd6e2;
    --page-light-bottom: #9fb0cb;
    --footer-blue: #0b3a7c;
    --night-top: #07070d;
    --night-mid: #141626;
    --tower-glow: #3b4256;
    --band-purple: #3a2a6e;
    --band-navy: #1b3a8c;
    --brand-blue: #3a6fd8;
    --white: #ffffff;
  }
  * { box-sizing: border-box; margin: 0; padding: 0; }
  html, body { width: 1200px; height: 1024px; overflow: hidden; }
  body {
    background: var(--stage);
    font-family: "Exo 2", sans-serif;
    color: var(--ink);
    position: relative;
  }
  .spread {
    position: absolute;
    left: 30px; top: 32px;
    width: 1140px; height: 960px;
    display: flex;
    box-shadow: 0 18px 40px rgba(0,0,0,0.18);
  }
  .page { position: relative; width: 570px; height: 960px; overflow: hidden; }

  /* Back page */
  .back-page__photo {
    position: absolute; inset: 0;
    background:
      radial-gradient(ellipse at 60% 30%, rgba(120,130,150,0.35), transparent 60%),
      linear-gradient(180deg, var(--page-light-top) 0%, var(--page-light-mid) 55%, var(--page-light-bottom) 100%);
  }
  .back-page__content {
    position: absolute; left: 103px; top: 118px; width: 362px;
  }
  .section-title {
    text-align: center; font-weight: 700; font-size: 17px; letter-spacing: 0.2px;
    margin-bottom: 58px;
  }
  .intro, .closing { font-size: 14px; line-height: 19px; text-align: justify; }
  .skills { list-style: none; font-size: 14px; line-height: 19px; margin: 20px 0 22px; }
  .skills li { padding-left: 9px; text-indent: -9px; }
  .skills li::before { content: "· "; }
  .contact {
    position: absolute; left: 0; width: 570px; top: 700px;
    text-align: center; font-size: 13.5px; line-height: 18px;
  }
  .contact__label { font-weight: 600; }
  .contact__block { margin-bottom: 14px; }
  .contact__row { display: flex; justify-content: center; gap: 44px; }
  .back-page__footer {
    position: absolute; left: 0; bottom: 0; width: 100%; height: 52px;
    background: var(--footer-blue); color: var(--white);
    display: flex; align-items: center; justify-content: center;
    font-size: 14px;
  }

  /* Cover page */
  .cover__photo {
    position: absolute; left: 0; top: 0; width: 100%; height: 776px;
    background:
      linear-gradient(100deg, transparent 35%, rgba(80,90,115,0.55) 45%, rgba(40,44,60,0.5) 60%, transparent 75%),
      linear-gradient(180deg, var(--night-top) 0%, var(--night-mid) 100%);
  }
  .cover__brand {
    position: absolute; left: 57px; top: 48px;
    display: flex; align-items: center; gap: 10px;
    color: var(--brand-blue); font-weight: 700; font-size: 22px; letter-spacing: 1px;
  }
  .cover__brand-mark { width: 26px; height: 26px; background: var(--brand-blue); }
  .cover__band {
    position: absolute; left: 0; top: 776px; width: 100%; height: 184px;
    background: linear-gradient(180deg, var(--band-purple) 0%, var(--band-navy) 100%);
    color: var(--white); text-align: center; padding: 46px 0 0 60px;
  }
  .cover__headline { font-size: 34px; line-height: 40px; font-weight: 700; }
  .cover__subline { font-size: 34px; line-height: 40px; font-weight: 400; }
</style>
</head>
<body>
  <main class="spread">
    <section class="page back-page">
      <div class="back-page__photo" role="img" aria-label="Faded photo of two colleagues reviewing work together in an office"></div>
      <div class="back-page__content">
        <h2 class="section-title">WHO IS NORVALE NETWORKS?</h2>
        <p class="intro">Norvale Networks is a growing organisation of experienced IT professionals. Our goal is to be a leading IT provider across the mid-market to enterprise segment. The professional skill sets retained by our team currently cover the following:</p>
        <ul class="skills">
          <li>Senior Consulting, Project and Program Management</li>
          <li>Senior Corvant expertise (CRE, CRP, CRA, CRS)</li>
          <li>Senior Panelis Specialists (PSE, PSA, PSP's)</li>
          <li>Technical Business Analysis, systems audit</li>
          <li>Systems &amp; Network specialists, on premises and cloud</li>
          <li>Disaster Recovery and Business Continuity.</li>
          <li>Sales, Account Management, Support in commercial SME, mid-market, enterprise, and government.</li>
        </ul>
        <p class="closing">Norvale Networks has a large Sales and Account Management team with sales support and technical pre-sales staff. Our goal is to nurture our customers and to have long term</p>
      </div>
      <div class="contact">
        <div class="contact__block">
          <div class="contact__label">ADDRESS</div>
          <div>Larkfield Head Office</div>
          <div>218-220 Ridgeway Road</div>
          <div>Larkfield, NSW, 2199</div>
        </div>
        <div class="contact__block">
          <div class="contact__label">Sales Office</div>
          <div>14 Harbour Lane</div>
          <div>Sydney NSW 2000</div>
        </div>
        <div class="contact__row">
          <div><div class="contact__label">PHONE</div><div>1300-418-672</div></div>
          <div><div class="contact__label">EMAIL</div><div>info@norvalenetworks.com.au</div></div>
        </div>
      </div>
      <footer class="back-page__footer">Visit us @ www.norvalenetworks.com.au</footer>
    </section>

    <section class="page cover">
      <div class="cover__photo" role="img" aria-label="Night photo of a twisting glass skyscraper with lit office windows"></div>
      <div class="cover__brand"><span class="cover__brand-mark"></span>NORVALE NETWORKS</div>
      <div class="cover__band">
        <p class="cover__headline">EMBRACE DIGITAL OR</p>
        <p class="cover__subline">RISK BEING LEFT BEHIND</p>
      </div>
    </section>
  </main>
</body>
</html>
```